Corvell Upholstery & Design
Stationary & Biz Card
Project: Corvell Upholstery & Design
Corvell Upholstery & Design -
Creative Brief
Bright & Fun-filled
Dorin Velasq
Owner
51847 Pellinore Court Sterling, VA 20166
dorin@corvellupholstery-example.com
www.corvellupholstery-example.com

```html
<!DOCTYPE html>
<html lang="en">
<head>
<meta charset="utf-8">
<title>Corvell Upholstery &amp; Design — Business Card</title>
<link rel="stylesheet" href="https://fonts.googleapis.com/css2?family=Open+Sans:wght@300;400;700&display=swap">
<style>
  :root {
    --backdrop: #ece9e4;
    --card-white: #ffffff;
    --brand-red: #e6222b;
    --rule-grey: #b9b9b9;
    --ink-grey: #5d5d5d;
    --text-white: #ffffff;
  }
  * { box-sizing: border-box; margin: 0; padding: 0; }
  html, body {
    width: 1200px; height: 780px; overflow: hidden;
    background: var(--backdrop);
    font-family: "Open Sans", Arial, sans-serif;
  }
  .canvas { position: relative; width: 1200px; height: 780px; }
  .business-card {
    position: absolute; left: 100px; top: 100px;
    width: 1000px; height: 580px;
    border-radius: 34px; overflow: hidden;
    background: var(--card-white);
    box-shadow: 0 10px 30px rgba(0,0,0,0.18);
  }
  .brand-area {
    position: absolute; left: 0; top: 0; width: 100%; height: 360px;
    display: flex; flex-direction: column; align-items: center; justify-content: center;
    gap: 26px;
  }
  .brand-dot {
    width: 70px; height: 70px; border-radius: 50%;
    background: var(--brand-red);
  }
  .brand-name {
    font-weight: 300; font-size: 38px; letter-spacing: 6px;
    color: var(--ink-grey); text-transform: uppercase;
  }
  .divider-band {
    position: absolute; left: 0; top: 360px; width: 100%; height: 6px;
    background: var(--rule-grey);
  }
  .contact-band {
    position: absolute; left: 0; top: 366px; width: 100%; height: 214px;
    background: var(--brand-red); color: var(--text-white);
  }
  .owner-block {
    position: absolute; right: 530px; top: 22px;
    text-align: right;
  }
  .owner-name { font-weight: 700; font-size: 27px; line-height: 34px; }
  .owner-title { font-weight: 400; font-size: 20px; line-height: 28px; }
  .owner-address { margin-top: 34px; font-size: 20px; line-height: 28px; }
  .column-rule {
    position: absolute; left: 500px; top: 20px; width: 2px; height: 174px;
    background: var(--text-white);
  }
  .contact-list {
    position: absolute; left: 528px; top: 16px; list-style: none;
  }
  .contact-list li {
    display: flex; align-items: center; gap: 12px;
    height: 36px; font-size: 20px;
  }
  .contact-list svg { width: 24px; height: 24px; flex: none; }
</style>
</head>
<body>
<div class="canvas">
  <div class="business-card">
    <div class="brand-area">
      <div class="brand-dot"></div>
      <div class="brand-name">Corvell Upholstery &amp; Design</div>
    </div>
    <div class="divider-band"></div>
    <div class="contact-band">
      <div class="owner-block">
        <p class="owner-name">Dorin Velasq</p>
        <p class="owner-title">Owner</p>
        <p class="owner-address">51847 Pellinore Court<br>Marlowe, VA 20899</p>
      </div>
      <div class="column-rule"></div>
      <ul class="contact-list">
        <li>
          <svg viewBox="0 0 24 24" aria-hidden="true"><path fill="#fff" d="M6.6 10.8c1.4 2.8 3.8 5.1 6.6 6.6l2.2-2.2c.3-.3.7-.4 1-.2 1.1.4 2.3.6 3.6.6.6 0 1 .4 1 1V20c0 .6-.4 1-1 1C10.6 21 3 13.4 3 4c0-.6.4-1 1-1h3.5c.6 0 1 .4 1 1 0 1.3.2 2.5.6 3.6.1.3 0 .7-.2 1z"/></svg>
          555-014-2201
        </li>
        <li>
          <svg viewBox="0 0 24 24" aria-hidden="true"><rect x="6" y="2" width="12" height="20" rx="2" fill="#fff"/><rect x="8" y="5" width="8" height="11" fill="#e6222b"/><circle cx="12" cy="19" r="1.2" fill="#e6222b"/></svg>
          555-014-2202
        </li>
        <li>
          <svg viewBox="0 0 24 24" aria-hidden="true"><rect x="7" y="3" width="10" height="6" fill="#fff"/><rect x="3" y="9" width="18" height="9" rx="2" fill="#fff"/><rect x="7" y="15" width="10" height="6" fill="#fff" stroke="#e6222b" stroke-width="1.2"/></svg>
          555-014-2203
        </li>
        <li>
          <svg viewBox="0 0 24 24" aria-hidden="true"><circle cx="12" cy="12" r="11" fill="#fff"/><text x="12" y="17" text-anchor="middle" font-family="Open Sans, Arial, sans-serif" font-weight="700" font-size="15" fill="#e6222b">@</text></svg>
          dorin@corvellupholstery-example.com
        </li>
        <li>
          <svg viewBox="0 0 24 24" aria-hidden="true"><circle cx="12" cy="12" r="10" fill="none" stroke="#fff" stroke-width="2"/><ellipse cx="12" cy="12" rx="4.5" ry="10" fill="none" stroke="#fff" stroke-width="1.6"/><line x1="2" y1="12" x2="22" y2="12" stroke="#fff" stroke-width="1.6"/></svg>
          www.corvellupholstery-example.com
        </li>
      </ul>
    </div>
  </div>
</div>
</body>
</html>
```